Brivoza banner and eDM design

We need banner ads and an eDM header to promote Brivoza.com.au (not currently live but logo and site design complete).

Banners should ideally be in flash with back-up gifs but we would be open to just animated gifs as well.

Banner sizes to be delivered are:
300x250
729x90
468x60
160x600

Best to keep banner file size under 25kb if possible (based on standard publisher specs)

For the eDM header, it should be around:
600 wide x
150-200 high

The advertising role is to promote the websites services which are related to making HR easy for small business owners - specifically relating to recruitment, induction, engagement and employee exit. I'll attach more details on this.

Target Market(s)

Small and medium business owners - slightly male skew

Industry/Entity Type

Small Business

Requirements
Must have
• Must match the look and feel and colour palette of the logo and website design that will be attached to this brief.

Must look professional

Must follow the copy guide for the frames as outlined in the attachment - there are 2 options for frame 3 listed. I'd like to get 2 sets of banners developed to cover both options.

Must have clear call-to-action
Nice to have
• Nice to have sophisticated animation if possible

I've added two potential images that could be used - either could be used to illustrate the 'Save time and improve results' line -
one focused on finding the right person
one is focused on improving results through a team

You could potentially use a screen grab of the site homepage in the design too - but only if eligible since none of the copy on it is finalised.

```html
<!DOCTYPE html>
<html lang="en">
<head>
<meta charset="utf-8">
<title>Brivoza banner set</title>
<link rel="stylesheet" href="https://fonts.googleapis.com/css2?family=Open+Sans:wght@700;800&family=Roboto+Condensed:wght@400&display=swap">
<style>
  :root {
    --sky: #41a8e1;
    --slate: #86878f;
    --logo-pale: #8cc3e6;
    --logo-deep: #3b6ea5;
    --band: #1470b8;
    --cta-top: #ffb347;
    --cta-bottom: #f0730a;
    --cta-edge: #b9560b;
    --frame: #2a2a2a;
    --paper: #ffffff;
    --art-light: #eef2f6;
    --art-mid: #c9d3dc;
    --art-blue: #5cb2ea;
  }
  * { box-sizing: border-box; margin: 0; padding: 0; }
  html, body {
    width: 960px; height: 1200px; overflow: hidden;
    background: var(--paper);
    font-family: "Open Sans", Arial, sans-serif;
  }
  .sheet { position: relative; width: 960px; height: 1200px; }
  .banner {
    position: absolute; left: 115px; width: 720px; height: 180px;
    border: 1px solid var(--frame); background: var(--paper); overflow: hidden;
  }
  .banner--1 { top: 37px; }
  .banner--2 { top: 277px; }
  .banner--3 { top: 517px; }
  .banner--4 { top: 757px; }
  .banner--5 { top: 997px; }

  .brand {
    position: absolute; left: 482px; top: 40px;
    display: flex; align-items: center; gap: 8px;
    color: var(--logo-pale); font-weight: 700; font-size: 38px; letter-spacing: -1px;
  }
  .brand__dot { width: 40px; height: 40px; border-radius: 50%; background: var(--logo-pale); }

  .cta {
    position: absolute; left: 488px; top: 100px; width: 206px; height: 40px;
    border: 1px solid var(--cta-edge); border-radius: 5px;
    background: linear-gradient(var(--cta-top), var(--cta-bottom));
    box-shadow: 2px 3px 4px rgba(0,0,0,.35);
    color: #fff; font-weight: 700; font-size: 21px; line-height: 38px; text-align: center;
    text-shadow: 0 1px 1px rgba(0,0,0,.35);
  }

  .art {
    position: absolute;
    background: linear-gradient(100deg, var(--art-light) 0%, var(--art-mid) 55%, var(--art-blue) 100%);
    border-radius: 4px;
  }
  .banner--1 .art { left: 170px; top: 30px; width: 290px; height: 150px; }
  .banner--2 .art { left: 280px; top: 14px; width: 186px; height: 166px; }

  .line { position: absolute; font-weight: 700; line-height: 1; white-space: nowrap; }
  .blue { color: var(--sky); }
  .grey { color: var(--slate); }

  .banner--1 .headline { left: 22px; top: 12px; font-size: 52px; color: var(--sky); font-weight: 800; }

  .banner--2 .headline { left: 14px; top: 8px; font-size: 54px; color: var(--sky); font-weight: 800; }
  .banner--2 .sub { left: 14px; top: 70px; font-size: 35px; color: var(--slate); }
  .banner--2 .big { left: 12px; top: 112px; font-size: 58px; color: var(--sky); font-weight: 800; }

  .banner--3 .intro { left: 16px; top: 22px; font-size: 29px; }
  .banner--3 .list1 { left: 14px; top: 72px; font-size: 33px; color: var(--sky); }
  .banner--3 .list2 { left: 14px; top: 118px; font-size: 33px; }

  .banner--4 .l1 { left: 16px; top: 12px; font-size: 46px; color: var(--slate); }
  .banner--4 .l1 .free { font-size: 72px; color: var(--sky); font-weight: 800; vertical-align: -4px; }
  .banner--4 .l2 { left: 16px; top: 94px; font-size: 36px; }
  .banner--4 .l3 { left: 186px; top: 134px; font-size: 36px; }

  .banner--5 .brand--large {
    left: 26px; top: 14px; gap: 14px; font-size: 72px; color: var(--logo-deep); letter-spacing: -2px;
  }
  .banner--5 .brand--large .brand__dot { width: 78px; height: 78px; background: var(--logo-deep); }
  .banner--5 .cta { top: 54px; }
  .band {
    position: absolute; left: 0; bottom: 0; width: 100%; height: 51px;
    background: var(--band); color: #fff;
    font-family: "Roboto Condensed", "Arial Narrow", sans-serif;
    font-size: 31px; letter-spacing: 1.5px; line-height: 51px; padding-left: 22px;
  }
</style>
</head>
<body>
<main class="sheet">

  <section class="banner banner--1">
    <div class="art" role="img" aria-label="Team of figures pulling a rope along a rising blue arrow"></div>
    <p class="line headline">Save time</p>
    <div class="brand"><span class="brand__dot"></span>Brivoza</div>
    <a class="cta">Find out more</a>
  </section>

  <section class="banner banner--2">
    <div class="art" role="img" aria-label="Team of figures pulling a rope along a rising blue arrow"></div>
    <p class="line headline">Save time</p>
    <p class="line sub">and improve</p>
    <p class="line big">RESULTS</p>
    <div class="brand"><span class="brand__dot"></span>Brivoza</div>
    <a class="cta">Find out more</a>
  </section>

  <section class="banner banner--3">
    <p class="line intro"><span class="grey">with </span><span class="blue">Brivoza</span><span class="grey"> Guides to...</span></p>
    <p class="line list1">Recruitment,</p>
    <p class="line list2"><span class="blue">Induction, </span><span class="grey">Exit </span><span class="blue">and more</span></p>
    <div class="brand"><span class="brand__dot"></span>Brivoza</div>
    <a class="cta">Find out more</a>
  </section>

  <section class="banner banner--4">
    <p class="line l1">Featuring <span class="free">FREE</span></p>
    <p class="line l2"><span class="grey">instructional </span><span class="blue">HR videos</span></p>
    <p class="line l3"><span class="grey">and </span><span class="blue">articles</span></p>
    <div class="brand"><span class="brand__dot"></span>Brivoza</div>
    <a class="cta">Find out more</a>
  </section>

  <section class="banner banner--5">
    <div class="brand brand--large"><span class="brand__dot"></span>Brivoza</div>
    <a class="cta">Find out more</a>
    <p class="band">Easy end to end HR solutions with Brivoza</p>
  </section>

</main>
</body>
</html>
```